mediation practice website build

Looking to create a website for new civil mediation practice. Pages would be "home", "about us", "about mediation", "scheduling" (perhaps with some kind of calendar function), "contact us". Would love to be able to update content/text myself.
Target Market(s)
Small to midsize businesses and attorneys representing those size businesses in pending disputes.
Industry/Entity Type
Build
Look and feel
Each slider illustrates characteristics of the customer's brand and the style your logo design should communicate.

```html
<!DOCTYPE html>
<html lang="en">
<head>
<meta charset="utf-8">
<title>Willowbend Mediation</title>
<link href="https://fonts.googleapis.com/css2?family=Arimo:wght@400;700&display=swap" rel="stylesheet">
<style>
  :root {
    --navy: #17456f;
    --navy-deep: #123a60;
    --tab: #3a6797;
    --tab-active: #17467c;
    --band: #8fa88c;
    --panel: #c6d5c6;
    --schedule: #769673;
    --news-bg: #9db39c;
    --button: #3d7644;
    --member: #1d4a22;
    --white: #ffffff;
    --photo-light: #a9c486;
    --photo-mid: #6e9648;
    --photo-dark: #35572c;
  }
  * { box-sizing: border-box; margin: 0; padding: 0; }
  html, body { width: 1200px; height: 1019px; overflow: hidden; background: var(--white); }
  body { position: relative; font-family: "Arimo", Arial, sans-serif; color: var(--navy); }

  .brand { position: absolute; left: 28px; top: 28px; font-weight: 700; font-size: 31px; line-height: 36px; letter-spacing: 1px; color: var(--navy); text-transform: uppercase; }

  .main-nav { position: absolute; left: 27px; top: 116px; height: 36px; }
  .main-nav a { position: absolute; top: 0; height: 36px; line-height: 36px; text-align: center; color: var(--white); font-size: 15px; text-decoration: none; }
  .main-nav svg { position: absolute; left: 0; top: 0; z-index: -1; }
  .main-nav .current { font-weight: 700; }

  .ticker { position: absolute; left: 27px; top: 151px; width: 1133px; height: 47px; background: var(--band); color: var(--navy); font-weight: 700; font-size: 15px; line-height: 47px; padding-left: 31px; white-space: nowrap; overflow: hidden; }

  .panel { position: absolute; top: 199px; height: 246px; background: var(--panel); }
  .whats-new { left: 27px; width: 373px; padding: 12px 15px 0 17px; }
  .whats-new h2 { font-size: 29px; font-weight: 700; color: var(--navy); margin-bottom: 21px; }
  .whats-new p { font-size: 14.5px; line-height: 15px; margin-bottom: 15px; }

  .schedule-panel { left: 406px; width: 375px; }
  .schedule { position: absolute; left: 38px; top: 9px; width: 295px; height: 227px; background: linear-gradient(180deg, #7b9b78, #6c8c69); box-shadow: 3px 4px 6px rgba(0,0,0,.35); color: var(--white); padding: 8px 0 0 22px; }
  .schedule h3 { font-size: 17px; font-weight: 700; margin-bottom: 8px; }
  .schedule dl { display: grid; grid-template-columns: 135px 1fr; font-size: 14.5px; line-height: 15px; }
  .schedule .gap { margin-top: 15px; }

  .login-panel { left: 787px; width: 373px; }
  .login-panel h3 { position: absolute; left: 72px; top: 35px; font-size: 17px; font-weight: 700; color: var(--member); }
  .field { position: absolute; left: 70px; width: 234px; height: 38px; background: var(--white); font-size: 14.5px; line-height: 38px; padding-left: 22px; color: #1b2a3a; }
  .field.user { top: 72px; }
  .field.pass { top: 132px; }
  .login-btn { position: absolute; left: 70px; top: 190px; width: 78px; height: 37px; background: var(--button); color: var(--white); font-weight: 700; font-size: 14.5px; line-height: 37px; text-align: center; box-shadow: 1px 2px 3px rgba(0,0,0,.35); }

  .feature { position: absolute; left: 27px; top: 454px; width: 1133px; height: 490px; background: linear-gradient(90deg, #aabfa9, var(--news-bg) 70%); }
  .feature-photo { position: absolute; left: 0; top: 0; }

  .latest-news { position: absolute; left: 783px; top: 30px; width: 340px; }
  .latest-news h2 { font-size: 29px; font-weight: 700; color: var(--navy); display: inline-block; padding-bottom: 4px; border-bottom: 1px solid var(--navy); margin-bottom: 18px; }
  .news-item { font-size: 14.5px; line-height: 15px; margin-bottom: 15px; color: var(--navy); }
  .news-item time { display: block; color: var(--white); }

  .footer-rule { position: absolute; left: 27px; top: 959px; width: 1133px; border-top: 1px solid var(--navy-deep); }
  .copyright { position: absolute; right: 40px; top: 973px; font-size: 14.5px; font-weight: 700; color: var(--navy-deep); }
</style>
</head>
<body>
  <div class="brand">Willowbend<br>Mediation</div>

  <nav class="main-nav">
    <svg width="700" height="36" viewBox="0 0 700 36" aria-hidden="true">
      <polygon points="0,0 126,0 136,12 136,36 0,36" fill="var(--tab-active)"/>
      <polygon points="139,0 263,0 273,12 273,36 139,36" fill="var(--tab)"/>
      <polygon points="278,0 403,0 413,12 413,36 278,36" fill="var(--tab)"/>
      <polygon points="417,0 541,0 551,12 551,36 417,36" fill="var(--tab)"/>
      <polygon points="555,0 679,0 689,12 689,36 555,36" fill="var(--tab)"/>
    </svg>
    <a class="current" style="left:0;width:124px" href="#">Home</a>
    <a style="left:139px;width:134px" href="#">About Mediation</a>
    <a style="left:278px;width:134px" href="#">Scheduling</a>
    <a style="left:417px;width:134px" href="#">Our Company</a>
    <a style="left:555px;width:134px" href="#">Contact Us</a>
  </nav>

  <div class="ticker">Looking to create a website for new civil mediation practice. Pages would be "home", "about us", "about mediation"........................................................</div>

  <section class="panel whats-new">
    <h2>What’s New</h2>
    <p>Looking to create a website for new civil mediation practice. Pages would be "home", "about us", "about mediation", "scheduling" (perhaps with some kind of calendar function), "contact us". Would love to be able to update content/text myself.</p>
    <p>Looking to create a website for new civil mediation practice. Pages would be "home", "about us", "about mediation", "scheduling" (perhaps with some kind of calendar function), "contact us". Would love to be able to update content/text myself.</p>
  </section>

  <section class="panel schedule-panel">
    <div class="schedule">
      <h3>Scheduling</h3>
      <dl>
        <dt>09.00 - 10.00</dt><dd>Mediation 1</dd>
        <dt>10.00 - 11.00</dt><dd>Mediation 2</dd>
        <dt>11.00 - 12.00</dt><dd>Mediation 3</dd>
        <dt class="gap">12.00 -13.00</dt><dd class="gap">Break</dd>
        <dt class="gap">13.00 - 14.00</dt><dd class="gap">Mediation 4</dd>
        <dt>14.00 - 15.00</dt><dd>Mediation 5</dd>
        <dt class="gap">15.00 - 16.00</dt><dd class="gap">Break</dd>
        <dt class="gap">16.00 - 17.00</dt><dd class="gap">Mediation 6</dd>
      </dl>
    </div>
  </section>

  <section class="panel login-panel">
    <h3>Member Login</h3>
    <div class="field user">User Name.............</div>
    <div class="field pass">Password.............</div>
    <div class="login-btn">LOGIN</div>
  </section>

  <section class="feature">
    <svg class="feature-photo" width="740" height="490" viewBox="0 0 740 490" role="img" aria-label="Photo of a peach tree branch with young green fruit and leaves">
      <defs>
        <linearGradient id="leafTones" x1="0" y1="0" x2="1" y2="1">
          <stop offset="0" stop-color="var(--photo-light)"/>
          <stop offset="0.5" stop-color="var(--photo-mid)"/>
          <stop offset="1" stop-color="var(--photo-dark)"/>
        </linearGradient>
        <filter id="dropShadow" x="-5%" y="-5%" width="115%" height="115%">
          <feDropShadow dx="3" dy="4" stdDeviation="3" flood-color="#000" flood-opacity="0.45"/>
        </filter>
      </defs>
      <polygon points="0,0 635,0 732,84 732,481 0,481" fill="url(#leafTones)" filter="url(#dropShadow)"/>
    </svg>

    <div class="latest-news">
      <h2>Lastest News</h2>
      <article class="news-item">Looking to create a website for new civil mediation practice. Pages would be "home", "about us", "about mediation", "scheduling" (perhaps with some kind of calendar function), "contact us". Would love to be able to update content/text myself.<time>08 May, 2011</time></article>
      <article class="news-item">Looking to create a website for new civil mediation practice. Pages would be "home", "about us", "about mediation", "scheduling" (perhaps with some kind of calendar function), "contact us". Would love to be able to update content/text myself.<time>06 May, 2011</time></article>
      <article class="news-item">Looking to create a website for new civil mediation practice. Pages would be "home", "about us", "about mediation", "scheduling" (perhaps with some kind of calendar function), "contact us". Would love to be able to update content/text myself.<time>02 May, 2011</time></article>
    </div>
  </section>

  <div class="footer-rule"></div>
  <footer class="copyright">© 2011 Willowbend Mediation. All rights reserved.</footer>
</body>
</html>
```